Business Card Design

Brambique is a floral design company for weddings and special events.
Colours wanted are dark grey, aqua blue, white and black.
dark grey for the background, and the Brambique in the aqua blue, rest of the writing in white and black etc.

Our floral design style is Rustic, textural, natural,
Wanting some kind of simplistic flower symbol next to the Brambique see pictures.

Hi im so sorry I've changed some criteria. been confused on how this site works and what i want!! hope this is more straight forward. I also need clip art of the simple floral design i attached for my web site and also car magnets. thank you thank you thank YOU!!!! cherrs Mel

I have attached x5 ideas on where to place the lotus flower next to and around the brambique. please use simliar colours of the flower as pictured. please cut out the white back ground from the flower. use only petals. use only lotus or the other icon provided per idea. still deciding on which one to use so waiting to see what looks best with your designs. thank you so very much in advance.!! Kindest REgards Mel

hi i am currently getting a logo design made through this also so can we wait until it is complete before any revisions are made. sorry about the delay!! thank you thank you thank you!! kind regards Mel

Reason: im having a logo made also to use on the cards. please hold off on any designs until this is received. thank you and so sorry about this!! cheers mEL

Target Market(s)

modern elegant professional

Industry/Entity Type

Floral

Contact Information for Business Card

Front:
brambique floral design (all lower case) floral design in smaller writting)
www.brambiquefloraldesign.example.au

Back:
Wedding and event design

Melissa - 0490582146
brambique@quillnet.example.au
Petra-0499365017
floristpetralowell@mailbay.example.com

Kelvara Heads, Coral Coast, QLD

Font styles to use
Other font styles liked:
• corben, cookie

Colors
87d0c7
34b8a4
eaf2ce
ffffff
e4daeb
cfdeed

Requirements
Must have
• ; dark grey for back ground. or possible all white?
;brambique floral designs in lower case and in blue' green aqua colour. all other writing in white.
icon which i can also use on the website. see pictures(i want to use the same on my web site.. if you can please make me an clip art icon also?
Nice to have
• simple elegant, earthy, flower icon
or second option icon of lotus looking flower brambique inside
fonts please: brambique floral design in (corben)
all writing on the back in (cookie)
maybe have the same icon clip art provided faintly on the back, bold on the front?
i also need car magnets to
Should not have

```html
<!DOCTYPE html>
<html lang="en">
<head>
<meta charset="utf-8">
<title>Brambique – Business Card</title>
<link rel="stylesheet" href="https://fonts.googleapis.com/css2?family=Oswald:wght@500;600&display=swap">
<style>
  :root {
    --surface: #eceded;
    --card: #bcbcbc;
    --ink: #1d1d1f;
    --aqua-blue: #3a7fcf;
    --mark: #e9e9e9;
  }
  * { margin: 0; padding: 0; box-sizing: border-box; }
  html, body {
    width: 1200px; height: 794px; overflow: hidden;
    background: var(--surface);
    font-family: "Oswald", "Arial Narrow", sans-serif;
  }
  .sheet {
    position: relative; width: 1200px; height: 794px;
    display: flex; align-items: center; justify-content: center; gap: 60px;
  }
  .card {
    position: relative; width: 520px; height: 298px;
    background: var(--card);
    box-shadow: 0 2px 6px rgba(0,0,0,0.12);
  }
  /* Back: contact details */
  .contacts {
    position: absolute; right: 34px; top: 30px;
    text-align: right; color: var(--ink);
    font-weight: 500; font-size: 13px; letter-spacing: 1.2px;
    line-height: 1.45; text-transform: uppercase;
  }
  .contacts .person { color: var(--aqua-blue); }
  .contacts .group { margin-bottom: 14px; }
  .contacts .location { margin-top: 30px; }
  /* Front: name and tagline */
  .identity {
    position: absolute; left: 0; right: 0; top: 78px;
    display: flex; align-items: center; justify-content: center; gap: 18px;
  }
  .brand-name {
    color: var(--aqua-blue);
    font-weight: 500; font-size: 92px; line-height: 1;
    letter-spacing: 1px;
  }
  .brand-dot { width: 26px; height: 26px; border-radius: 50%; background: var(--mark); }
  .tagline {
    position: absolute; left: 0; right: 0; top: 212px;
    text-align: center; color: var(--ink);
    font-weight: 600; font-size: 9.5px; letter-spacing: 1.3px;
    text-transform: uppercase;
  }
</style>
</head>
<body>
  <main class="sheet">
    <section class="card card-back" aria-label="Card back">
      <div class="contacts">
        <div class="group">
          <p class="person">Mel</p>
          <p>0490582146</p>
          <p>brambique@quillnet.example.au</p>
        </div>
        <div class="group">
          <p class="person">Petra</p>
          <p>0499365017</p>
          <p>floristpetralowell@mailbay.example.com</p>
        </div>
        <p class="location">Kelvara Heads, Coral Coast, QLD</p>
      </div>
    </section>

    <section class="card card-front" aria-label="Card front">
      <div class="identity">
        <h1 class="brand-name">brambique</h1>
        <span class="brand-dot" aria-hidden="true"></span>
      </div>
      <p class="tagline">Floral designers weddings and special events web site address is to come</p>
    </section>
  </main>
</body>
</html>
```